Bravel Acres Business Cards

design business cards for our new business should match my Corvane Quotations business cards

Contact Information for Business Card

2817 W 68th N St
Tulsa, OK 74592

Requirements
Must have
• should match logo colors

```html
<!DOCTYPE html>
<html lang="en">
<head>
<meta charset="utf-8">
<title>Bravel Acres – Business Cards</title>
<link rel="stylesheet" href="https://fonts.googleapis.com/css2?family=Montserrat:wght@500;600;700;800&display=swap">
<style>
  :root {
    --green: #7ac943;
    --teal: #1ba5a8;
    --ink: #050505;
    --deep-teal: #0f2c34;
    --leaf-grey: #3c3c3c;
    --white: #ffffff;
    --stage: #d4d4d4;
  }
  * { box-sizing: border-box; margin: 0; padding: 0; }
  html, body {
    width: 1200px; height: 1200px; overflow: hidden;
    background: var(--stage);
    font-family: "Montserrat", Arial, sans-serif;
  }
  .sheet {
    position: relative; width: 1200px; height: 1200px;
    display: flex; flex-direction: column; align-items: center;
    justify-content: center; gap: 70px;
  }
  .card {
    position: relative; width: 880px; height: 500px; overflow: hidden;
    box-shadow: 0 10px 28px rgba(0,0,0,.25);
  }
  .card--front { background: var(--ink); }
  .card--contact { background: var(--deep-teal); }
  .card__bands { position: absolute; inset: 0; width: 100%; height: 100%; }
  .leaf-field {
    position: absolute; left: 40px; right: 40px; top: 60px; bottom: 60px;
    background: radial-gradient(ellipse at center, #1a1a1a 0%, #232323 55%, #111 100%);
  }
  .wordmark {
    position: absolute; color: var(--green); font-weight: 800;
    text-transform: uppercase; white-space: nowrap;
  }
  .card--front .wordmark {
    left: 0; right: 0; top: 205px; text-align: center;
    font-size: 66px; letter-spacing: 8px;
  }
  .card--contact .wordmark {
    left: 60px; top: 222px; font-size: 40px; letter-spacing: 4px;
  }
  .web {
    position: absolute; left: 60px; bottom: 9px;
    color: var(--white); font-weight: 700; font-size: 22px; letter-spacing: .5px;
  }
  .contact {
    position: absolute; left: 520px; top: 96px; color: var(--white);
  }
  .contact__name {
    font-size: 30px; font-weight: 800; text-transform: uppercase; letter-spacing: 1px;
    line-height: 1;
  }
  .contact__name .first { color: var(--green); }
  .contact__name .last { color: var(--teal); }
  .contact__role { font-size: 17px; font-weight: 600; margin: 6px 0 22px; }
  .contact__row {
    display: flex; align-items: flex-start; gap: 14px;
    font-size: 15px; font-weight: 500; line-height: 1.35; margin-bottom: 14px;
  }
  .contact__icon {
    flex: 0 0 28px; width: 28px; height: 28px; border-radius: 50%;
    background: var(--leaf-grey);
    display: flex; align-items: center; justify-content: center;
  }
  .contact__icon svg { width: 16px; height: 16px; }
  .contact__text { padding-top: 4px; }
</style>
</head>
<body>
<main class="sheet">

  <section class="card card--contact" aria-label="Business card, contact side">
    <svg class="card__bands" viewBox="0 0 880 500" aria-hidden="true">
      <polygon points="0,0 470,0 452,17 0,17" fill="var(--green)"/>
      <polygon points="480,0 880,0 880,36 446,36" fill="var(--teal)"/>
      <polygon points="0,458 458,458 498,500 0,500" fill="var(--green)"/>
      <polygon points="476,480 880,480 880,500 496,500" fill="var(--teal)"/>
    </svg>
    <div class="wordmark">Bravel Acres</div>
    <div class="contact">
      <div class="contact__name"><span class="first">Dana</span> <span class="last">Merrow</span></div>
      <div class="contact__role">President</div>
      <div class="contact__row">
        <span class="contact__icon"><svg viewBox="0 0 24 24"><path fill="var(--green)" d="M6.6 10.8a15.1 15.1 0 0 0 6.6 6.6l2.2-2.2a1 1 0 0 1 1-.25 11.4 11.4 0 0 0 3.6.57 1 1 0 0 1 1 1V20a1 1 0 0 1-1 1A17 17 0 0 1 3 4a1 1 0 0 1 1-1h3.5a1 1 0 0 1 1 1c0 1.25.2 2.45.57 3.57a1 1 0 0 1-.25 1z"/></svg></span>
        <span class="contact__text">555-214-7730</span>
      </div>
      <div class="contact__row">
        <span class="contact__icon"><svg viewBox="0 0 24 24"><rect x="3" y="5" width="18" height="14" rx="2" fill="var(--green)"/><path d="M3.5 6l8.5 7 8.5-7" stroke="var(--leaf-grey)" stroke-width="2" fill="none"/></svg></span>
        <span class="contact__text">DMerrow@bravelacres.com</span>
      </div>
      <div class="contact__row">
        <span class="contact__icon"><svg viewBox="0 0 24 24"><path fill="var(--green)" d="M12 2a7 7 0 0 0-7 7c0 5.2 7 13 7 13s7-7.8 7-13a7 7 0 0 0-7-7zm0 9.5A2.5 2.5 0 1 1 12 6.5a2.5 2.5 0 0 1 0 5z"/></svg></span>
        <span class="contact__text">2817 W 68th N St<br>Tulsa, OK 74592</span>
      </div>
    </div>
    <div class="web">WWW.BRAVELACRES.COM</div>
  </section>

  <section class="card card--front" aria-label="Business card, brand side">
    <div class="leaf-field" role="img" aria-label="Repeating pattern of grey leaf shapes across the black card"></div>
    <svg class="card__bands" viewBox="0 0 880 500" aria-hidden="true">
      <polygon points="0,0 470,0 452,17 0,17" fill="var(--green)"/>
      <polygon points="480,0 880,0 880,36 446,36" fill="var(--teal)"/>
      <polygon points="0,458 458,458 498,500 0,500" fill="var(--green)"/>
      <polygon points="476,480 880,480 880,500 496,500" fill="var(--teal)"/>
    </svg>
    <div class="wordmark">Bravel Acres</div>
    <div class="web">WWW.BRAVELACRES.COM</div>
  </section>

</main>
</body>
</html>
```